Web Page needed for Dr. Wanbrook Consult

The company works in the consultant business for processes in large projects our of engineering and construction business. We develop strategies but work also in critical projects to get them right.
The page should have a modern appearance but though a classy and luxury touch.
Updates

The project was bought in a package, logo plus web page. Now the designers do submit logos again, although the logo has been set. This part is only the web site. I changed the text to clarify it, I contacted support to put that right, but that needs an extension of minimum 7 days to catch up.

Due to the confusion in the project, it was first set up as logo project and later corrected (I have no clue how that happened, as I bought a package with logo + web, and logo is already done), there is a large delay in getting feedback. Please be so kind and extend until 31.01. In Europe there is holidays until 07.01. and I have no time to discuss the topics with my client until 10.01., than we need to feed in response and get changes done.

Logo Text

The logo is already fixed, I asked for web page.

Number of Pages Required

5+ page

Font styles to use
Sans Serif

Colors

Designer to choose colors to be used in the design.

Requirements
Must have
• Home/Start
• Lean Construction
• Lean Equipment
• Lean Design
• Lean Training
• Team
• Contact
• Imprint
Nice to have
• Darker color, luxury appearance, please integrate the logo in the attachment here.
• I would like to have a web page with animated context, such as this one here: https://tovalmerworks.example

```html
<!DOCTYPE html>
<html lang="en">
<head>
<meta charset="utf-8">
<title>Dr. Wanbrook Consult</title>
<link rel="stylesheet" href="https://fonts.googleapis.com/css2?family=Cinzel:wght@400;500&family=Montserrat:wght@500;600;700&family=Arimo:wght@400&display=swap">
<style>
:root{
  --blue:#2c5ea6;
  --blue-deep:#1d4580;
  --navy:#132644;
  --navy-dark:#0d1b33;
  --green:#7dbd2e;
  --text:#4a4a4a;
  --white:#ffffff;
  --muted:#b8c8e2;
}
*{box-sizing:border-box;margin:0;padding:0}
html,body{width:1200px;height:3587px;overflow:hidden}
body{position:relative;background:var(--white);font-family:"Arimo",Arial,sans-serif;color:var(--text)}
.abs{position:absolute}
.serif{font-family:"Cinzel",Georgia,serif;font-weight:400;letter-spacing:1px}

/* header */
.site-header{position:absolute;left:0;top:0;width:1200px;height:93px;background:var(--white)}
.brand{position:absolute;left:140px;top:23px;display:flex;align-items:center;gap:9px}
.brand-mark{width:24px;height:24px;background:var(--blue);flex:none}
.brand-name{font-family:"Montserrat",Arial,sans-serif;font-weight:600;font-size:18px;line-height:21px;color:var(--blue);letter-spacing:.5px}
.main-nav a{position:absolute;top:41px;font-size:15px;color:#222;text-decoration:none;font-family:"Arimo",Arial,sans-serif}
.main-nav a.active{color:var(--blue)}
.main-nav a.active::after{content:"";position:absolute;left:-2px;right:-2px;top:27px;height:2px;background:var(--green)}

/* hero */
.hero-photo{left:0;top:93px;width:1200px;height:610px;background:linear-gradient(110deg,#2d4b78 0%,#5a6d83 35%,#c9c94a 60%,#2e4a78 85%,#5e6f84 100%)}
.hero-panel{left:0;top:203px;width:526px;height:362px;background:rgba(37,73,128,.88);border-radius:0 200px 200px 0/0 181px 181px 0}
.hero-title{left:135px;top:284px;color:var(--white);font-size:39px;line-height:47.5px}
.btn{position:absolute;display:flex;align-items:center;justify-content:center;font-family:"Montserrat",Arial,sans-serif;font-weight:600;text-decoration:none;border-radius:30px}
.btn-hero{left:135px;top:443px;width:163px;height:46px;background:var(--blue);color:var(--white);font-size:14px}
.slider-dots{left:563px;top:651px;display:flex;gap:8px}
.slider-dots span{width:13px;height:13px;border-radius:50%;background:var(--white)}
.slider-dots span.off{background:transparent;border:2px solid var(--white)}

/* who */
.who-visual{left:166px;top:789px;width:344px;height:343px;background:linear-gradient(135deg,#8fa6c4,#c6cfb2 55%,#e1b049);border-radius:0 172px 172px 0}
.who-title{left:561px;top:808px;font-size:36px;color:#243447}
.who-text{left:567px;width:460px;font-size:15px;line-height:27px;color:#4a4a4a}
.btn-outline-green{left:562px;top:1062px;width:165px;height:52px;border:2px solid var(--green);color:var(--green);font-size:15px}

/* services */
.services{left:0;top:1215px;width:1200px;height:525px;background:linear-gradient(120deg,#2a63a8 0%,#234f8c 55%,#14243f 100%)}
.section-title{font-size:34px;color:var(--white);text-align:center;width:1200px;left:0}
.service-icon{width:110px;height:100px}
.service-name{font-family:"Montserrat",Arial,sans-serif;font-weight:600;font-size:17px;color:var(--white)}
.service-text{width:270px;font-size:14.5px;line-height:22px;color:var(--muted)}
.btn-outline-white{width:138px;height:42px;border:2px solid var(--white);color:var(--white);font-size:12px}

/* why */
.why-photo{left:0;top:1740px;width:1200px;height:550px;background:linear-gradient(100deg,#c9d34a 0%,#d9d6c4 30%,#b7a98e 60%,#e3cfa6 100%)}
.why-panel{left:612px;top:1814px;width:588px;height:383px;background:rgba(44,94,166,.93);border-radius:200px 0 0 200px/192px 0 0 192px}
.why-title{left:724px;top:1890px;font-size:33px;color:var(--white)}
.why-text{left:729px;top:1944px;width:390px;font-size:15px;line-height:24.7px;color:var(--white)}
.why-btn{left:728px;top:2084px;width:149px;height:43px;font-size:13px}

/* projects */
.projects-title{top:2352px;color:var(--blue);font-size:34px}
.project-tile{top:2418px;width:309px;height:280px}
.tile-a{left:118px;background:linear-gradient(180deg,#3d7fd8,#7aa5d8 50%,#8b8b84)}
.tile-b{left:445px;background:linear-gradient(180deg,#4b7fc0,#6b7d88)}
.tile-c{left:771px;background:linear-gradient(180deg,#2b74d3,#5a8fd4 50%,#2a3f7a)}
.tile-overlay{left:445px;top:2418px;width:309px;height:280px;background:rgba(19,54,110,.85)}
.tile-frame{left:455px;top:2428px;width:289px;height:260px;border:2px solid rgba(255,255,255,.85)}
.tile-title{left:445px;top:2518px;width:309px;text-align:center;font-family:"Montserrat",Arial,sans-serif;font-weight:600;font-size:17px;color:var(--white)}
.tile-text{left:495px;top:2553px;width:210px;text-align:center;font-size:14.5px;line-height:23px;color:var(--white)}

/* contact */
.contact{left:0;top:2795px;width:1200px;height:792px;background:linear-gradient(180deg,#132340 0%,#1a2f52 50%,#203a63 100%)}
.contact-title{top:2864px}
.field{position:absolute;border:1.5px solid rgba(255,255,255,.75);border-radius:24px;color:var(--white);font-size:15px;padding-left:24px;display:flex;align-items:center}
.field-message{align-items:flex-start;padding-top:18px;border-radius:18px}
.btn-submit{left:518px;top:3210px;width:174px;height:49px;background:var(--green);color:var(--white);font-size:17px}

/* footer */
.footer-band{left:0;top:3310px;width:1200px;height:277px}
.footer-brand{left:0;top:3372px;width:1200px;display:flex;justify-content:center;align-items:center;gap:8px}
.footer-brand span.mark{width:16px;height:16px;background:var(--white)}
.footer-brand span.name{font-family:"Montserrat",Arial,sans-serif;font-weight:600;font-size:17px;color:var(--white)}
.footer-nav a{position:absolute;top:3444px;font-size:15px;color:var(--white);text-decoration:none}
.copyright{left:0;top:3479px;width:1200px;text-align:center;font-size:12.5px;color:var(--white)}
.social{left:505px;top:3514px;display:flex;gap:10px}
.social span{width:36px;height:36px;border-radius:50%;background:#0c0c0c}
</style>
</head>
<body>

<header class="site-header">
  <div class="brand"><span class="brand-mark"></span><span class="brand-name">DR. WANBROOK<br>CONSULT</span></div>
  <nav class="main-nav">
    <a class="active" href="#" style="left:454px">HOME</a>
    <a href="#" style="left:539px">ABOUT US</a>
    <a href="#" style="left:654px">SERVICES</a>
    <a href="#" style="left:768px">PROJECTS</a>
    <a href="#" style="left:887px">BLOG</a>
    <a href="#" style="left:969px">CONTACT US</a>
  </nav>
</header>

<section class="hero">
  <div class="abs hero-photo" role="img" aria-label="Photo of two engineers in hard hats and hi-vis jackets reviewing a laptop in an industrial hall"></div>
  <div class="abs hero-panel"></div>
  <h1 class="abs serif hero-title">CONSULTING IN<br>ENGINEERING AND<br>CONSTRUCTION</h1>
  <a class="btn btn-hero" href="#">LEARN MORE</a>
  <div class="abs slider-dots"><span></span><span></span><span></span><span class="off"></span></div>
</section>

<section class="who">
  <div class="abs who-visual" role="img" aria-label="Photo of a construction site worker framed in a rounded shape"></div>
  <h2 class="abs serif who-title">WHO WE ARE</h2>
  <p class="abs who-text" style="top:872px">Nunc tempus felis vitae urna Vivamus porttitor neque at volutpat rutrum purus nisi eleifend libero a tempus libero lectus</p>
  <p class="abs who-text" style="top:955px">Morbi diam mauris viverra in gravida eu mattis in ante Morbi eget arcu Morbi porta libero id ullamcorper nonummy nibh ligula pulvinar metus eget consectetuer augue nisi quis lacus Ut ac mi quis l</p>
  <a class="btn btn-outline-green" href="#">LEARN MORE</a>
</section>

<section class="abs services"></section>
<h2 class="abs serif section-title" style="top:1280px">OUR SERVICES</h2>

<svg class="abs service-icon" style="left:164px;top:1366px" viewBox="0 0 110 100" fill="none" stroke="#fff" stroke-width="2">
  <path d="M6 98V48a46 46 0 0 1 92 0v6" stroke="#9fb7da" stroke-width="3"/>
  <rect x="32" y="35" width="44" height="40"/><path d="M40 67l26-26M62 38l7 7M45 70h26M66 52v18"/>
</svg>
<svg class="abs service-icon" style="left:478px;top:1366px" viewBox="0 0 110 100" fill="none" stroke="#fff" stroke-width="2">
  <path d="M6 98V48a46 46 0 0 1 92 0v6" stroke="#9fb7da" stroke-width="3"/>
  <circle cx="40" cy="44" r="9"/><circle cx="40" cy="44" r="3"/><path d="M40 31v5M40 52v5M27 44h5M48 44h5"/>
  <path d="M52 82v-12a12 12 0 0 1 24 0v12z"/><circle cx="64" cy="52" r="8"/>
</svg>
<svg class="abs service-icon" style="left:798px;top:1366px" viewBox="0 0 110 100" fill="none" stroke="#fff" stroke-width="2">
  <path d="M6 98V48a46 46 0 0 1 92 0v6" stroke="#9fb7da" stroke-width="3"/>
  <circle cx="54" cy="58" r="20"/><path d="M46 68v-8M52 68v-12M58 68v-16M64 68v-20M44 52l10-8 8 4 8-8"/>
</svg>

<h3 class="abs service-name" style="left:165px;top:1492px">CONSTRUCTION BUSINESS</h3>
<h3 class="abs service-name" style="left:476px;top:1492px">ENGINEERING PROJECTS</h3>
<h3 class="abs service-name" style="left:798px;top:1492px">DEVELOPMENT</h3>
<p class="abs service-text" style="left:162px;top:1524px">Nunc tempus felis vitae urna Vivamus porttitor neque at volutpat rutrum purus nisi eleifend libero a tempus</p>
<p class="abs service-text" style="left:476px;top:1524px">Nunc tempus felis vitae urna Vivamus porttitor neque at volutpat rutrum purus nisi eleifend libero a tempus</p>
<p class="abs service-text" style="left:796px;top:1524px">Nunc tempus felis vitae urna Vivamus porttitor neque at volutpat rutrum purus nisi eleifend libero a tempus</p>
<a class="btn btn-outline-white" href="#" style="left:160px;top:1605px">LEARN MORE</a>
<a class="btn btn-outline-white" href="#" style="left:474px;top:1605px">LEARN MORE</a>
<a class="btn btn-outline-white" href="#" style="left:794px;top:1613px">LEARN MORE</a>

<section class="why">
  <div class="abs why-photo" role="img" aria-label="Photo of a surveyor in a hard hat using a total station on a building site"></div>
  <div class="abs why-panel"></div>
  <h2 class="abs serif why-title">WHY WE ARE</h2>
  <p class="abs why-text">Nunc tempus felis vitae urna Vivamus porttitor neque at volutpat rutrum purus nisi eleifend libero a tempus libero lectus Morbi diam mauris viverra in gravida eu mattis in ante Morbi eget arcu Morbi porta libero id ullamcorper nonummy nibh ligula pulvinar metus eget</p>
  <a class="btn btn-outline-white why-btn" href="#">LEARN MORE</a>
</section>

<section class="projects">
  <h2 class="abs serif section-title projects-title">OUR PROJECTS</h2>
  <div class="abs project-tile tile-a" role="img" aria-label="Photo of a high-rise concrete building under construction with cranes"></div>
  <div class="abs project-tile tile-b" role="img" aria-label="Photo of a building under construction with scaffolding"></div>
  <div class="abs project-tile tile-c" role="img" aria-label="Photo of a steel-frame structure with cranes against a blue sky"></div>
  <div class="abs tile-overlay"></div>
  <div class="abs tile-frame"></div>
  <h3 class="abs tile-title">PROJECT TITLE</h3>
  <p class="abs tile-text">Nunc tempus felis vitae urna Vivamus porttitor neque</p>
</section>

<section class="abs contact" role="img" aria-label="Dark blue toned photo of engineers on site behind the contact form"></section>
<h2 class="abs serif section-title contact-title">CONTACT US</h2>
<div class="field" style="left:237px;top:2936px;width:357px;height:46px">First Name</div>
<div class="field" style="left:605px;top:2936px;width:358px;height:46px">Last Name</div>
<div class="field" style="left:237px;top:2996px;width:357px;height:47px">Email address</div>
<div class="field" style="left:605px;top:2996px;width:358px;height:47px">Phone Number</div>
<div class="field field-message" style="left:238px;top:3060px;width:724px;height:128px">Message</div>
<a class="btn btn-submit" href="#">SUBMIT</a>

<svg class="abs footer-band" viewBox="0 0 1200 277" preserveAspectRatio="none">
  <polygon points="0,103 600,10 1200,103 1200,277 0,277" fill="#2c5ea6"/>
  <polyline points="0,103 600,10 1200,103" fill="none" stroke="#7dbd2e" stroke-width="6"/>
</svg>
<div class="abs footer-brand"><span class="mark"></span><span class="name">DR. WANBROOK CONSULT</span></div>
<nav class="footer-nav">
  <a href="#" style="left:301px">HOME</a>
  <a href="#" style="left:386px">ABOUT US</a>
  <a href="#" style="left:502px">SERVICES</a>
  <a href="#" style="left:616px">PROJECTS</a>
  <a href="#" style="left:734px">BLOG</a>
  <a href="#" style="left:816px">CONTACT US</a>
</nav>
<p class="abs copyright">© 2019 Company Name&nbsp; All right reserved</p>
<div class="abs social"><span aria-label="Social link"></span><span aria-label="Social link"></span><span aria-label="Social link"></span><span aria-label="Social link"></span></div>

</body>
</html>
```